Bramwell HVAC Service LLC Business Card

We just got a design created by one of your designers for a logo and now would like help with a business card design. The information to be included on the card is as follows:
Bramwell HVAC Service LLC (I will attach logo design)
P.O. Box 482
Dunmore, CO 80634
(970) 347-6159
Lonnie Tadwick
I might include an e-mail address, but I'm not sure yet.
Target Market(s)
Customers needing service or repairs done on their heating and air conditioning systems.
Industry/Entity Type
Business
Contact Information for Business Card
P.O. Box 482
Dunmore, CO 80634
(970) 347-6159
Lonnie Tadwick

```html
<!DOCTYPE html>
<html lang="en">
<head>
<meta charset="utf-8">
<title>Bramwell HVAC Service LLC – Business Card</title>
<link rel="stylesheet" href="https://fonts.googleapis.com/css2?family=Arimo:wght@400;700&display=swap">
<style>
  :root {
    --navy: #002157;
    --red: #ed1c24;
    --white: #ffffff;
    --sun: #fde3a6;
    --frost: #9cc3ff;
  }
  html, body {
    margin: 0;
    padding: 0;
    width: 1200px;
    height: 693px;
    overflow: hidden;
    background: var(--white);
  }
  .card {
    position: relative;
    width: 1200px;
    height: 693px;
    overflow: hidden;
    background: var(--white);
    font-family: "Arimo", Arial, sans-serif;
  }
  .card__bands,
  .card__emblem {
    position: absolute;
    left: 0;
    top: 0;
  }
  .card__bands { width: 1200px; height: 693px; }
  .card__emblem { width: 460px; height: 460px; }

  .brand {
    position: absolute;
    left: 462px;
    top: 50px;
    display: flex;
    align-items: center;
    gap: 18px;
  }
  .brand__mark {
    width: 34px;
    height: 34px;
    border-radius: 50%;
    background: var(--navy);
  }
  .brand__name {
    margin: 0;
    font-size: 40px;
    font-weight: 700;
    letter-spacing: 0.5px;
    color: var(--navy);
    white-space: nowrap;
  }

  .contact {
    position: absolute;
    left: 556px;
    top: 412px;
    margin: 0;
    padding: 0;
    list-style: none;
    color: var(--white);
  }
  .contact__row {
    display: flex;
    align-items: center;
    height: 66px;
  }
  .contact__icon {
    width: 60px;
    flex: none;
    display: flex;
    justify-content: center;
    margin-right: 26px;
  }
  .contact__name  { font-size: 54px; letter-spacing: 0.5px; }
  .contact__phone { font-size: 43px; }
  .contact__email { font-size: 32px; }

  .address {
    position: absolute;
    left: 300px;
    top: 632px;
    display: flex;
    align-items: center;
    gap: 18px;
    color: var(--white);
    font-size: 34px;
    font-style: normal;
  }
</style>
</head>
<body>
<main class="card">

  <svg class="card__emblem" viewBox="0 0 460 460" role="img" aria-label="Sun with snowflake emblem, warm and cool climate illustration">
    <defs>
      <radialGradient id="emblemGlow" cx="0.32" cy="0.3" r="0.7">
        <stop offset="0" stop-color="var(--frost)"/>
        <stop offset="0.3" stop-color="#e9f1ff"/>
        <stop offset="0.45" stop-color="var(--sun)"/>
        <stop offset="1" stop-color="var(--sun)" stop-opacity="0"/>
      </radialGradient>
    </defs>
    <circle cx="140" cy="140" r="310" fill="url(#emblemGlow)"/>
  </svg>

  <svg class="card__bands" viewBox="0 0 1200 693" aria-hidden="true">
    <path class="band band--navy" d="M0,548 C450,510 900,300 1200,96 L1200,693 L0,693 Z" fill="var(--navy)"/>
    <path class="band band--red" d="M0,570 Q600,600 1200,640 L1200,693 L0,693 Z" fill="var(--red)"/>
  </svg>

  <header class="brand">
    <span class="brand__mark"></span>
    <h1 class="brand__name">Bramwell HVAC Service LLC</h1>
  </header>

  <ul class="contact">
    <li class="contact__row">
      <span class="contact__icon">
        <svg width="54" height="50" viewBox="0 0 56 52" aria-hidden="true">
          <circle cx="28" cy="6" r="5" fill="var(--white)"/>
          <circle cx="6" cy="14" r="4" fill="var(--white)"/>
          <circle cx="50" cy="14" r="4" fill="var(--white)"/>
          <path d="M6,18 L15,38 L41,38 L50,18 L38,28 L28,11 L18,28 Z" fill="var(--white)"/>
          <rect x="13" y="42" width="30" height="7" rx="2" fill="var(--white)"/>
        </svg>
      </span>
      <span class="contact__name">LONNIE TADWICK</span>
    </li>
    <li class="contact__row">
      <span class="contact__icon">
        <svg width="54" height="40" viewBox="0 0 54 40" aria-hidden="true">
          <path d="M2,12 Q27,-2 52,12 L48,18 L40,16 L38,10 Q27,7 16,10 L14,16 L6,18 Z" fill="var(--white)"/>
          <path d="M16,16 L38,16 L48,36 Q48,40 44,40 L10,40 Q6,40 6,36 Z" fill="var(--white)"/>
          <circle cx="27" cy="28" r="6" fill="var(--navy)"/>
        </svg>
      </span>
      <span class="contact__phone">(970) 347-6159</span>
    </li>
    <li class="contact__row">
      <span class="contact__icon">
        <svg width="52" height="34" viewBox="0 0 52 34" aria-hidden="true">
          <rect x="2" y="2" width="48" height="30" fill="none" stroke="var(--white)" stroke-width="3"/>
          <path d="M2,2 L26,20 L50,2 M2,32 L20,16 M50,32 L32,16" fill="none" stroke="var(--white)" stroke-width="3"/>
        </svg>
      </span>
      <span class="contact__email">lonnie_bramwellhvac@inboxmail.net</span>
    </li>
  </ul>

  <address class="address">
    <svg width="46" height="42" viewBox="0 0 46 42" aria-hidden="true">
      <path d="M23,2 L2,21 L7,21 L23,7 L39,21 L44,21 Z" fill="var(--white)"/>
      <rect x="32" y="4" width="6" height="10" fill="var(--white)"/>
      <path d="M9,23 L23,11 L37,23 L37,41 L27,41 L27,29 L19,29 L19,41 L9,41 Z" fill="var(--white)"/>
    </svg>
    <span class="address__text">P.O. Box 482 Dunmore, CO 80634</span>
  </address>

</main>
</body>
</html>
```